TRIVAN 2026 Flyer for Conference

TRIVAN needs a design for a 1-page flyer that we will hand out at an upcoming event & then later post online as a pdf. There are 3 elements which need to be on the flyer:

1) A logo. This should be prominent on the design (e.g., in the middle). The flyer should use the colors that are in that logo (e.g., for accents, design elements, and/or text; not all of these have to be used):
Dark blue: #185577
Med blue: #327C9A
Teal: #4EB1C2
Light Teal: #9EDBE6

2) The conference theme -- Forests of Wonder: Climbing toward Research Fluency -- should be at the flyer's top.

3) Finally, these six tracks should be listed below the theme and the logo (it's font size should be at least a couple sizes smaller than the size used for the theme):
- Pearls of Pedagogy: Teaching Techniques that Work
- The Depth Gauge: Measuring Instructional Impact
- Techtonic Shifts: Innovation and Educational Technology
- Captain's Log: Navigating Leadership in Library Instruction
- Swimming Together: Collaborating with Others
- The Bermuda Triangle: Exploring (Seemingly) Eternal Challenges

Font styles to use
Sans Serif

Colors
0094D4
00A9DD
6FCCEA
C7EBF8
E9F6FB

Requirements
Must have
• The 3 elements listed in the description: 1) the logo, 2) the text of the theme and 3) the text for the tracks.

```html
<!DOCTYPE html>
<html lang="en">
<head>
<meta charset="utf-8">
<title>TRIVAN 2026 – Conference Flyer</title>
<link rel="stylesheet" href="https://fonts.googleapis.com/css2?family=Roboto+Condensed:wght@400&family=Lexend:wght@400;500&display=swap">
<style>
  :root {
    --dark-blue: #185577;
    --med-blue: #327C9A;
    --teal: #4EB1C2;
    --light-teal: #9EDBE6;
    --header-bg: #d0ebf1;
    --card-bg: #eef7fa;
    --card-border: #d5e9ef;
    --ink: #1e1e1e;
    --faint: #d3e8ef;
    --white: #ffffff;
  }
  * { margin: 0; padding: 0; box-sizing: border-box; }
  html, body { width: 952px; height: 1200px; overflow: hidden; background: var(--white); }
  .flyer { position: relative; width: 952px; height: 1200px; background: var(--white); font-family: "Lexend", sans-serif; }

  .theme-band { position: absolute; top: 0; left: 0; width: 100%; height: 190px; background: var(--header-bg); text-align: center; }
  .theme-title { font-family: "Roboto Condensed", sans-serif; font-weight: 400; color: var(--dark-blue); font-size: 56px; line-height: 74px; padding-top: 22px; letter-spacing: 0.3px; }

  .brand { position: absolute; top: 268px; left: 0; width: 100%; display: flex; justify-content: center; align-items: center; gap: 18px; }
  .brand-dot { width: 34px; height: 34px; border-radius: 50%; background: var(--teal); }
  .brand-name { font-family: "Lexend", sans-serif; font-weight: 500; font-size: 72px; color: var(--dark-blue); letter-spacing: 1px; }

  .tracks-heading { position: absolute; top: 455px; width: 100%; text-align: center; font-family: "Roboto Condensed", sans-serif; font-weight: 400; font-size: 60px; color: var(--ink); }

  .tracks { position: absolute; top: 558px; left: 48px; width: 857px; display: grid; grid-template-columns: 419px 419px; column-gap: 19px; row-gap: 26px; list-style: none; }
  .track { height: 122px; background: var(--card-bg); border: 1.5px solid var(--card-border); padding: 0 18px; display: flex; flex-direction: column; justify-content: center; }
  .track-name { font-size: 20px; font-weight: 500; color: var(--dark-blue); line-height: 28px; }
  .track-desc { font-size: 15.5px; font-weight: 500; color: var(--ink); line-height: 26px; }

  .footer-wave { position: absolute; left: 0; top: 980px; width: 952px; height: 220px; }
  .footer-mark { position: absolute; top: 1045px; left: 690px; font-family: "Lexend", sans-serif; font-weight: 500; font-size: 30px; color: var(--faint); }
  .contact-label { position: absolute; top: 1090px; left: 48px; font-size: 18px; font-weight: 500; color: var(--teal); }
  .contact-phone { position: absolute; top: 1120px; left: 48px; display: flex; align-items: center; gap: 16px; font-family: "Roboto Condensed", sans-serif; font-size: 44px; color: var(--teal); }
  .contact-email { position: absolute; top: 1158px; right: 60px; display: flex; align-items: center; gap: 9px; font-size: 14px; color: var(--white); font-family: "Lexend", sans-serif; font-weight: 400; }
</style>
</head>
<body>
<main class="flyer">
  <header class="theme-band">
    <h1 class="theme-title">Forests of Wonder:<br>Climbing toward Research Fluency</h1>
  </header>

  <div class="brand" aria-label="TRIVAN 2026">
    <span class="brand-dot"></span>
    <span class="brand-name">TRIVAN 2026</span>
  </div>

  <h2 class="tracks-heading">The Six Tracks</h2>

  <ul class="tracks">
    <li class="track"><span class="track-name">Pearls of Pedagogy</span><span class="track-desc">Teaching Techniques that Work</span></li>
    <li class="track"><span class="track-name">The Depth Gauge</span><span class="track-desc">Measuring Instructional Impact</span></li>
    <li class="track"><span class="track-name">Techtonic Shifts</span><span class="track-desc">Innovation &amp; Educational Technology</span></li>
    <li class="track"><span class="track-name">Captain's Log</span><span class="track-desc">Navigating Leadership in Library Instruction</span></li>
    <li class="track"><span class="track-name">Swimming Together</span><span class="track-desc">Collaborating with Others</span></li>
    <li class="track"><span class="track-name">The Bermuda Triangle</span><span class="track-desc">Exploring (Seemingly) Eternal Challenges</span></li>
  </ul>

  <svg class="footer-wave" viewBox="0 0 952 220" aria-hidden="true">
    <path d="M0,92 C120,40 260,28 420,48 C600,72 760,170 860,160 C900,156 930,140 952,128 L952,220 L0,220 Z" fill="var(--dark-blue)"/>
    <path d="M55,34 C200,-5 380,20 560,70 C720,115 820,150 890,140" fill="none" stroke="var(--teal)" stroke-width="5" stroke-linecap="round"/>
  </svg>
  <div class="footer-mark">TRIVAN 2026</div>

  <p class="contact-label">For More Information Contact Us</p>
  <p class="contact-phone">
    <svg width="44" height="44" viewBox="0 0 44 44" aria-hidden="true">
      <circle cx="22" cy="22" r="20" fill="none" stroke="var(--teal)" stroke-width="2.5"/>
      <path d="M16 12 l4 0 l2 6 l-3 2 c1.5 3.5 3.5 5.5 7 7 l2 -3 l6 2 l0 4 c0 1 -1 2 -2 2 c-10 -0.5 -17 -7.5 -18 -18 c0 -1 1 -2 2 -2 z" fill="var(--teal)"/>
    </svg>
    <span>0131 496 0123</span>
  </p>
  <p class="contact-email">
    <svg width="18" height="14" viewBox="0 0 18 14" aria-hidden="true">
      <rect x="0.5" y="0.5" width="17" height="13" rx="1.5" fill="var(--light-teal)"/>
      <path d="M1 1.5 L9 8 L17 1.5" fill="none" stroke="var(--dark-blue)" stroke-width="1.5"/>
    </svg>
    <span>hello@trivan-conf.org</span>
  </p>
</main>
</body>
</html>
```